Pharmacy

Two sided postcard. Pictures on one side. Description on the other. We design and build pharmacies. pictures are some of our finished work. You can use as many pictures as you like not necessary to use all of them. Size of card should be 5"x7". See my website at display@brightmorefixtures.com for more inspiration. I include the back of one card that I used recently. Both sids need design input. Feel free to contact me with questions.
Requirements
Must have
- Must be a two sided postcard
Nice to have
- I am sending a design of a sleek type postcard that I saw online as an example.
- https://pixlink.example/images/k7WqRt
- I am looking for something modern.
- Not limited to colors on my website.

```html
<!DOCTYPE html>
<html lang="en">
<head>
<meta charset="utf-8">
<title>Brightmore Display &amp; Fixture Co Inc. — Postcard</title>
<link href="https://fonts.googleapis.com/css2?family=Cinzel:wght@600;700&family=Cabin:ital,wght@0,400;0,700;1,700&display=swap" rel="stylesheet">
<style>
  :root {
    --maroon: #7d0b0e;
    --cream: #f6efdd;
    --paper: #ffffff;
    --backdrop: #fbf8d6;
    --ink-light: #ffffff;
    --photo-wood: #8a4a30;
    --photo-light: #d9d4c8;
  }
  * { box-sizing: border-box; margin: 0; padding: 0; }
  html, body { width: 1200px; height: 696px; overflow: hidden; }
  body { background: var(--backdrop); position: relative; font-family: "Cabin", sans-serif; }

  .card {
    position: absolute; top: 155px; width: 540px; height: 386px;
    background: var(--paper); overflow: hidden;
    box-shadow: 0 2px 8px rgba(0,0,0,.18);
  }
  .card--back { left: 40px; }
  .card--front { left: 620px; }

  /* Back side */
  .title-band {
    position: absolute; left: 0; top: 0; width: 300px; height: 72px;
    background: var(--maroon); color: var(--ink-light);
    padding: 12px 14px; font-family: "Cinzel", serif; font-weight: 700;
    font-size: 17px; line-height: 1.15; letter-spacing: .5px;
  }
  .motto {
    position: absolute; left: 14px; top: 82px;
    font-family: "Cinzel", serif; font-weight: 700; font-size: 12.5px;
    color: var(--maroon); letter-spacing: .4px;
  }
  .about {
    position: absolute; left: 14px; top: 106px; width: 280px; height: 176px;
    background: var(--cream); color: var(--maroon);
    padding: 10px 14px; font-size: 12px; line-height: 1.6; text-align: justify;
  }
  .phone-bar {
    position: absolute; left: 0; top: 290px; width: 310px; height: 42px;
    background: var(--maroon); color: var(--ink-light);
    padding-left: 16px; font-weight: 700; font-style: italic; font-size: 30px; line-height: 42px;
  }
  .contact {
    position: absolute; font-family: "Cinzel", serif; font-weight: 700;
    color: var(--maroon); font-size: 10.5px; line-height: 1.35; letter-spacing: .3px;
  }
  .card--back .contact { left: 16px; top: 340px; }
  .return-address {
    position: absolute; left: 318px; top: 16px;
    font-size: 8px; line-height: 1.9; color: var(--maroon);
  }
  .stamp-box {
    position: absolute; right: 26px; top: 36px; width: 70px; height: 86px;
    border: 1px solid #333;
  }

  /* Front side */
  .store-photo {
    position: absolute; left: 0; top: 0; width: 262px; height: 386px;
    background: linear-gradient(150deg, var(--photo-light) 0%, #c3b39a 35%, var(--photo-wood) 70%, #3a3432 100%);
  }
  .front-art { position: absolute; left: 250px; top: 0; }
  .front-title {
    position: absolute; left: 272px; top: 10px; width: 260px;
    font-family: "Cinzel", serif; font-weight: 700; font-size: 16px; line-height: 1.15;
    color: var(--maroon); letter-spacing: .4px;
  }
  .front-tagline {
    position: absolute; left: 262px; top: 60px; width: 278px; height: 42px;
    display: flex; align-items: center; justify-content: center; text-align: center;
    font-family: "Cinzel", serif; font-weight: 700; font-size: 11.5px; line-height: 1.25;
    color: var(--ink-light);
  }
  .card--front .contact { right: 14px; top: 334px; color: var(--ink-light); text-align: right; font-size: 11px; }
</style>
</head>
<body>

<section class="card card--back" aria-label="Postcard back">
  <div class="title-band">Brightmore Display &amp;<br>Fixture Co Inc.</div>
  <p class="motto">Quality-Experience-Innovation</p>
  <p class="about">Family owned and operated for three generations - Brightmore Display &amp; Fixture Co. Inc. is the oldest store fixture company in New Jersey. As designers &amp; manufacturers we can save you hours of time and money. Our level of experience will be evident from the outset and you will be pleased that you found us. We look forward to hearing from you.</p>
  <div class="phone-bar">201 555 0148</div>
  <p class="contact">display@brightmorefixtures.com<br>www.brightmorefixtures.com</p>
  <address class="return-address">Brightmore Display &amp;<br>Fixture Co. Inc.<br>PO Box 318 Ridgefield<br>NJ 07657</address>
  <div class="stamp-box"></div>
</section>

<section class="card card--front" aria-label="Postcard front">
  <div class="store-photo" role="img" aria-label="Photo of a finished pharmacy interior with wood shelving and a counter"></div>
  <svg class="front-art" width="290" height="386" viewBox="0 0 290 386">
    <rect width="290" height="386" fill="var(--maroon)"/>
    <rect x="12" y="0" width="278" height="58" fill="var(--cream)"/>
    <polygon points="12,104 290,104 290,322 80,322 12,254" fill="var(--cream)"/>
    <g stroke="#fff" stroke-width="4">
      <polygon role="img" aria-label="Photo of pharmacy checkout area" transform="translate(70,196)" points="-38,0 -19,-33 19,-33 38,0 19,33 -19,33" fill="#8c6a4e"/>
      <polygon role="img" aria-label="Photo of wood and green shelving unit" transform="translate(150,154)" points="-38,0 -19,-33 19,-33 38,0 19,33 -19,33" fill="#7f6a48"/>
      <polygon role="img" aria-label="Photo of cosmetics wall display" transform="translate(230,132)" points="-38,0 -19,-33 19,-33 38,0 19,33 -19,33" fill="#a99a92"/>
      <polygon role="img" aria-label="Photo of glass display cases" transform="translate(150,246)" points="-38,0 -19,-33 19,-33 38,0 19,33 -19,33" fill="#6f6a7a"/>
      <polygon role="img" aria-label="Photo of store aisle with shelving" transform="translate(230,224)" points="-38,0 -19,-33 19,-33 38,0 19,33 -19,33" fill="#9b7a62"/>
    </g>
  </svg>
  <h1 class="front-title">Brightmore Display &amp; Fixture Co Inc.</h1>
  <p class="front-tagline">A Complete Service From Design<br>Thru Installation</p>
  <p class="contact">display@brightmorefixtures.com<br>www.brightmorefixtures.com</p>
</section>

</body>
</html>
```